Wordpress Design Project - Development Company

We need a website for our Developments company "KT Developments". I would like to use Wordpress for its simplicity to update and added features.
We develop/build and sell Townhouses/Houses and Land around Brisbane, Qld. Initially we require a Web presence with no advanced features. We will develop the user logins and other features at a future point in time. We are undecided on having a single page with most of the detail or to have more detail on linked pages, we will review the options put forward. We have added a Sitemap and possible Frontpage sketch
Some sites for examples we have thought work similar and well:
http://www.brimfield.com.au/index.htm
http://tallowmeadow.com.au/
http://www.pmcorrigan.com.au
http://nexcrafta.com.au/
http://www.halvery.com.au/queensland.aspx
http://www.orbelyne.com.au/
I've attached our newly created Business Cards and we are also working on a logo for the company within the next couple of days which may or may not be the same as the Business Card
Any questions please ask
Updates
Please update the main picture on your webpages to the attached so we can compare equally http://files.quillbox.net/u/55720194/Img1c.jpg
Target Market(s)
Townhouse/House/Land buyers & Salespeople
Industry/Entity Type
Business
Look and feel

```html
<!DOCTYPE html>
<html lang="en">
<head>
<meta charset="utf-8">
<title>KT Developments P/L</title>
<link rel="stylesheet" href="https://fonts.googleapis.com/css2?family=Arimo:ital,wght@0,400;0,700;1,700&family=Archivo+Black&display=swap">
<style>
:root{
  --bg:#0d0e0f;
  --header:#050607;
  --panel:#242526;
  --panel-line:#4a4b4c;
  --text:#d6d6d6;
  --muted:#a9a9a9;
  --white:#ffffff;
  --tab-top:#f4f6f6;
  --tab-bot:#d9dede;
  --tab-active:#8d9090;
  --teal-top:#5ec0cc;
  --teal-bot:#2f8f9c;
  --grey-top:#7a7b7c;
  --grey-bot:#4a4b4c;
  --frame:#c9d3d6;
  --brand-square:#5ec0cc;
}
*{box-sizing:border-box;margin:0;padding:0}
html,body{width:1091px;height:1200px;overflow:hidden}
body{background:var(--bg);font-family:"Arimo",Arial,sans-serif;color:var(--text);position:relative}
.abs{position:absolute}

.site-header{left:0;top:0;width:1091px;height:68px;background:linear-gradient(#15181b,var(--header))}
.brand{left:24px;top:0;height:64px;display:flex;align-items:center;gap:14px;z-index:2}
.brand-square{width:22px;height:22px;background:var(--brand-square)}
.brand-name{font-family:"Arimo",sans-serif;font-weight:400;font-size:26px;color:var(--white)}
.header-shade{left:0;top:68px;width:1091px;height:100px;background:linear-gradient(#1c1e20,#111213)}

.main-nav{left:22px;top:120px;height:40px;display:flex;z-index:3}
.main-nav a{display:flex;align-items:center;justify-content:center;height:40px;font-size:14px;color:#111;text-decoration:none;background:linear-gradient(var(--tab-top),var(--tab-bot));border:1px solid #9aa;border-radius:5px 5px 0 0}
.main-nav a.active{background:linear-gradient(#2b2d2e,var(--tab-active));color:#111}
.dropdown{left:139px;top:160px;width:112px;height:58px;background:linear-gradient(#7b7e7f,#b7baba);padding:6px 6px;z-index:5}
.dropdown li{list-style:none;font-size:10px;color:#111;line-height:23px;padding-left:10px;position:relative}
.dropdown li::before{content:"";position:absolute;left:1px;top:8px;border:3px solid transparent;border-left:4px solid #111}

.hero{left:22px;top:171px;width:1045px;height:361px;border:3px solid var(--frame);background:linear-gradient(#3a86cf 0%,#8fc2e8 22%,#3d6d3a 40%,#2f5d2c 52%,#3fb3d2 60%,#1b86b8 85%,#14658e)}
.hero-caption{left:25px;top:465px;width:1039px;height:64px;background:rgba(20,40,55,.75);color:var(--white);font-size:20px;padding:21px 0 0 52px}
.slide-arrow{width:40px;height:40px;border-radius:50%;background:rgba(225,225,225,.85);display:flex;align-items:center;justify-content:center}
.dots{left:455px;top:556px;display:flex;gap:22px}
.dots i{width:12px;height:12px;border-radius:50%;background:#4f5b5d;border:1px solid #7a8a8c}
.dots i.on{background:#f2f2f2}

.project-card{top:592px;height:188px;border:2px solid #2b2c2d}
.project-card.teal{background:linear-gradient(var(--teal-top),var(--teal-bot))}
.project-card.grey{background:linear-gradient(var(--grey-top),var(--grey-bot))}
.project-card h2{position:absolute;left:8px;top:16px;font-family:"Archivo Black",sans-serif;font-style:italic;font-size:15px;color:var(--white);letter-spacing:.3px}
.project-card ul{position:absolute;left:12px;top:56px}
.project-card li{list-style:none;font-size:13px;color:var(--white);line-height:37px;padding-left:13px;position:relative}
.project-card li::before{content:"";position:absolute;left:0;top:15px;border:3px solid transparent;border-left:4px solid var(--white)}
.project-card li.link{text-decoration:underline}
.project-card .thumb{position:absolute;left:177px;top:56px;width:160px;height:92px;border:2px solid #2f4043}
.project-card .view-all{position:absolute;left:0;bottom:0;width:100%;height:25px;background:rgba(0,0,0,.18);text-align:center;font-family:"Archivo Black",sans-serif;font-style:italic;font-size:10px;line-height:25px;color:#173a40}
.project-card.grey .view-all{color:#111;background:linear-gradient(#6d6e6f,#a7a8a9)}

.content-panel{left:21px;top:800px;width:816px;height:318px;background:var(--panel)}
.section-title{font-family:"Archivo Black",sans-serif;font-style:italic;font-size:14px;color:var(--white)}
.about-text{left:39px;top:848px;width:558px;font-size:11px;line-height:24px;text-align:justify;color:var(--text)}
.about-thumb{left:615px;top:813px;width:209px;height:127px;border:2px solid #555}
.divider{left:39px;top:964px;width:784px;height:1px;background:var(--panel-line)}
.vdivider{left:466px;top:976px;width:1px;height:132px;background:var(--panel-line)}
.contact-lines{left:39px;top:1008px;font-size:11px;line-height:24px}
.cta-note{left:291px;top:1012px;font-size:11px}
.btn{display:flex;align-items:center;justify-content:center;border-radius:5px;background:linear-gradient(#8f9091,#2d2e2f);color:var(--white);font-family:"Archivo Black",sans-serif;font-style:italic;border:1px solid #111}
.btn-click{left:303px;top:1044px;width:130px;height:31px;font-size:12px}
.mail-input{left:479px;top:1011px;width:164px;height:27px;background:#5b5c5d;border-radius:4px;font-size:10px;color:#ddd;padding:8px 10px}
.btn-subscribe{left:650px;top:1011px;width:87px;height:26px;font-size:10px;font-family:"Arimo",sans-serif;font-style:normal;font-weight:700}
.stay-note{left:484px;top:1052px;font-size:11px;color:var(--muted)}

.categories{left:854px;top:814px}
.categories ul{margin-top:15px}
.categories li{list-style:none;font-size:11px;color:var(--text);line-height:32.7px;padding-left:14px;position:relative}
.categories li::before{content:"";position:absolute;left:0;top:13px;border:3px solid transparent;border-left:4px solid var(--text)}

.site-footer{left:0;top:1143px;width:1091px;height:57px;background:linear-gradient(#1c1d1e,#141516)}
.copyright{left:25px;top:1165px;font-size:10px;color:var(--text)}
.social{left:804px;top:1158px;display:flex;align-items:center;gap:12px;font-size:10px}
.social i{width:24px;height:24px;border-radius:50%;display:block}
</style>
</head>
<body>
<header>
  <div class="abs site-header"></div>
  <div class="abs brand"><span class="brand-square"></span><span class="brand-name">KT Developments P/L</span></div>
  <div class="abs header-shade"></div>
  <nav class="abs main-nav">
    <a style="width:117px" href="#">Home</a>
    <a class="active" style="width:112px" href="#">Overview</a>
    <a style="width:177px" href="#">Current Projects</a>
    <a style="width:190px" href="#">Completed Projects</a>
    <a style="width:163px" href="#">Future Projects</a>
    <a style="width:143px" href="#">Latest News</a>
    <a style="width:143px" href="#">Contact Us</a>
  </nav>
</header>

<section>
  <div class="abs hero" role="img" aria-label="Resort swimming pool with palm trees and a clubhouse"></div>
  <div class="abs hero-caption">Cicero are also reproduced in their exact original form...</div>
  <div class="abs slide-arrow" style="left:39px;top:333px"><svg width="14" height="14" viewBox="0 0 14 14"><path d="M9 2 4 7l5 5" fill="none" stroke="#333" stroke-width="3"/></svg></div>
  <div class="abs slide-arrow" style="left:1007px;top:333px"><svg width="14" height="14" viewBox="0 0 14 14"><path d="M5 2l5 5-5 5" fill="none" stroke="#333" stroke-width="3"/></svg></div>
  <div class="abs dots"><i class="on"></i><i></i><i></i><i></i><i></i><i></i></div>
</section>

<ul class="abs dropdown"><li>KT Developments</li><li>Halden Builders</li></ul>

<section>
  <article class="abs project-card teal" style="left:22px;width:347px">
    <h2>CURRENT PROJECTS</h2>
    <ul><li class="link">Lorem Ipsum Contantry</li><li>Lorem Ipsum Contantry</li><li>Lorem Ipsum Contantry</li></ul>
    <div class="thumb" role="img" aria-label="Two-storey family house with lawn" style="background:linear-gradient(#7fb0dc,#5c7b4b 55%,#3e6a2f)"></div>
    <div class="view-all">VIEW ALL</div>
  </article>
  <article class="abs project-card grey" style="left:373px;width:344px">
    <h2>COMPLETED PROJECTS</h2>
    <ul><li class="link">Lorem Ipsum Contantry</li><li>Lorem Ipsum Contantry</li><li>Lorem Ipsum Contantry</li></ul>
    <div class="thumb" role="img" aria-label="Mediterranean style villa with palms" style="background:linear-gradient(#5f9fd6,#d8b98a 50%,#5d6b45)"></div>
    <div class="view-all">VIEW ALL</div>
  </article>
  <article class="abs project-card grey" style="left:721px;width:345px">
    <h2>FUTURED PROJECTS</h2>
    <ul><li class="link">Lorem Ipsum Contantry</li><li>Lorem Ipsum Contantry</li><li>Lorem Ipsum Contantry</li></ul>
    <div class="thumb" role="img" aria-label="White villa with pool" style="background:linear-gradient(#5b8fd0,#e2e4e4 45%,#3fb6d8)"></div>
    <div class="view-all">VIEW ALL</div>
  </article>
</section>

<main>
  <div class="abs content-panel"></div>
  <h2 class="abs section-title" style="left:39px;top:817px">ABOUT US</h2>
  <p class="abs about-text">It is a long established fact that a reader will be distracted by the readable content of a page when looking at its layout. The point of using Lorem Ipsum is that it has a more-or-less normal distribution of letters, as 'lorem ipsum' will uncover many web sites still in their infancy. Various versions have evolved over the years, sometimes by accident, sometimes on purpose.</p>
  <div class="abs about-thumb" role="img" aria-label="Luxury white home with swimming pool" style="background:linear-gradient(#4f86c8,#ece4d2 45%,#2fa7c8 80%,#556b3b)"></div>
  <div class="abs divider"></div>
  <div class="abs vdivider"></div>

  <h2 class="abs section-title" style="left:39px;top:978px">CONTACT US</h2>
  <p class="abs contact-lines">The point of using Lorem Ipsum<br>normal distribution of letters<br>uncover many<br>Contact : 3900 12 12 &nbsp;(or) &nbsp;0400 555 019</p>
  <p class="abs cta-note">If You want to finish a project.</p>
  <a class="abs btn btn-click">CLICK HERE</a>

  <h2 class="abs section-title" style="left:479px;top:978px">STAY UPDATED</h2>
  <div class="abs mail-input">Enter your mail ID</div>
  <a class="abs btn btn-subscribe">SUBSCRIBE</a>
  <p class="abs stay-note">The point of using Lorem Ipsum is that it has a more-or-less</p>

  <aside class="abs categories">
    <h2 class="section-title">OUR CATAGORIES</h2>
    <ul>
      <li>Lorem Ipsum Contantry Popular</li><li>Lorem Ipsum Contantry Popular</li>
      <li>Lorem Ipsum Contantry Popular</li><li>Lorem Ipsum Contantry Popular</li>
      <li>Lorem Ipsum Contantry Popular</li><li>Lorem Ipsum Contantry Popular</li>
      <li>Lorem Ipsum Contantry Popular</li><li>Lorem Ipsum Contantry Popular</li>
    </ul>
  </aside>
</main>

<footer>
  <div class="abs site-footer"></div>
  <p class="abs copyright">Copyright © 2011 www.ktdevelopments-qld.com All rights reserved</p>
  <div class="abs social">
    <span>Connect with us :</span>
    <i style="background:#3b5b9a"></i><i style="background:#33b5e5"></i><i style="background:#f08a1c"></i><i style="background:#2f6fc0"></i><i style="background:#3a3d40"></i>
  </div>
</footer>
</body>
</html>
```